brightleafwell.com and taverclinic.com

I'd like to do a web design re-make on two of our websites. Brightleafwell.com is focused on selling nutriceutical products (private labeled by brightleafwell.com), and provide an expert blog to give great advices on general health.

Taverclinic.com is a site for Dr. Taver's new medicine clinic. It should be integrated with brightleafwell.com. Clients can directly make appointments on the site, and order products from brightleafwell.com.

Target Market(s)

Middle to upper

Industry/Entity Type

Clinic

Number of Pages Required

4 page

Font styles to use
Serif
Sans Serif

Colors
0254a3
0792cd
33a6d7
00a98f
33b7a4
acd036
9bcb3c
cadf82

Requirements
Must have
• Home page tabs: About Dr. Taver, Store, Blog, Videos, Appointment
• Home page content should include: a promotional section (with moving features), an appointment book (for online appointment booking), a product section (for store), and a blog section.
Nice to have
• The look and feel should be modern, professional, trustworthy, zen.
Should not have
• Real pictures of people, except for Dr. Taver.

```html
<!DOCTYPE html>
<html lang="en">
<head>
<meta charset="utf-8">
<title>Brightleaf Well — Integrative Medicine</title>
<link rel="stylesheet" href="https://fonts.googleapis.com/css2?family=Francois+One&family=Open+Sans:ital,wght@0,400;0,600;0,700;1,400&display=swap">
<style>
:root{
  --blue:#1b90e0;
  --blue-dark:#1577c0;
  --ink:#2b2b2b;
  --footer:#252525;
  --panel:#333333;
  --text:#555555;
  --muted:#8c8c8c;
  --line:#e3e3e3;
  --white:#ffffff;
}
*{box-sizing:border-box;margin:0;padding:0}
html,body{width:790px;height:1200px;overflow:hidden;background:var(--white)}
body{position:relative;font-family:"Open Sans",Arial,sans-serif;color:var(--text);font-size:11px}
.abs{position:absolute}

/* top bar */
.topbar{left:0;top:0;width:790px;height:21px;background:var(--ink);color:#ddd;font-size:10px}
.topbar .phone{left:87px;top:4px;display:flex;align-items:center;gap:6px}
.topbar .social{right:86px;top:5px;display:flex;gap:10px}
.topbar .social span{width:10px;height:10px;border-radius:50%;background:#ddd;display:block}

/* header */
.brand{left:85px;top:27px;font-family:"Francois One",Arial,sans-serif;font-size:21px;line-height:22px;color:var(--ink);letter-spacing:.5px}
.nav{left:390px;top:21px;height:58px;display:flex}
.nav a{display:flex;flex-direction:column;align-items:center;justify-content:center;gap:5px;background:var(--blue);color:var(--white);text-decoration:none;font-size:11px;height:58px;padding:0 11px;border-left:1px solid rgba(255,255,255,.35)}
.nav a:first-child{border-left:0}

/* hero */
.hero{left:0;top:79px;width:790px;height:254px;background:linear-gradient(90deg,#dfe8f1 0%,#8fb3d6 30%,#3f78b4 60%,#2f69a7 100%)}
.hero-text{right:88px;top:152px;text-align:right;color:var(--white)}
.hero-text h1{font-family:"Francois One",Arial,sans-serif;font-weight:400;font-size:21px;line-height:24px}
.hero-text p{font-family:"Francois One",Arial,sans-serif;font-size:12px;line-height:15px;margin-top:4px}
.dots{right:89px;top:257px;display:flex;gap:5px}
.dots span{width:6px;height:6px;background:var(--white)}

/* section titles */
.section-title{font-family:"Francois One",Arial,sans-serif;font-weight:400;font-size:16px;color:var(--blue);border-left:2px solid var(--ink);padding-left:7px;line-height:16px}

/* products */
.arrows{left:451px;top:365px;display:flex;gap:2px}
.arrows span{width:14px;height:14px;background:var(--blue);color:#fff;font-size:10px;line-height:14px;text-align:center}
.product{width:104px;top:393px}
.product .shot{height:140px;background:linear-gradient(180deg,#f4f4f4,#e8ecef)}
.product .label{height:24px;background:var(--blue);color:var(--white);font-family:"Francois One",Arial,sans-serif;font-size:10.5px;line-height:24px;text-align:center;white-space:nowrap}
.product p{font-style:italic;font-size:8.5px;line-height:11px;color:#444;margin-top:5px;width:104px}
.shop{margin-top:9px;display:flex;align-items:flex-end}
.shop span{display:inline-block;background:var(--ink);color:#fff;font-family:"Francois One",Arial,sans-serif;font-size:9px;padding:4px 7px;letter-spacing:.5px}
.shop i{flex:0 0 38px;border-bottom:1px solid var(--line);height:1px}

/* appointment */
.appt-intro{left:508px;top:395px;width:196px;font-style:italic;font-size:8.5px;line-height:11px;color:#444}
.form{left:508px;top:440px;width:196px}
.field{display:flex;height:26px;border:1px solid var(--line);border-top:0}
.field:first-child{border-top:1px solid var(--line)}
.field .ico{width:26px;display:flex;align-items:center;justify-content:center;background:var(--ink)}
.field .ico.alt{background:var(--blue)}
.field .ph{padding-left:8px;line-height:24px;font-size:8.5px;color:#aaa}
.field.msg{height:58px}
.field.msg .ico{align-items:flex-start;padding-top:5px;background:var(--ink)}
.btn{background:var(--blue);color:var(--white);font-family:"Francois One",Arial,sans-serif;font-size:9px;letter-spacing:.5px;text-align:center;line-height:25px;height:25px;white-space:nowrap}

/* about */
.about-box{left:87px;top:679px;width:396px;height:157px;border:1px solid var(--line)}
.video{left:100px;top:690px;width:172px;height:120px;background:#111}
.video .frame{position:absolute;left:3px;top:3px;right:3px;bottom:16px;background:linear-gradient(135deg,#d9d3c6,#8c7a62 55%,#c08c52)}
.video .bar{position:absolute;left:5px;right:5px;bottom:4px;height:8px;display:flex;align-items:center;gap:5px;color:#ccc;font-size:6px}
.video .bar i{flex:1;height:2px;background:#555}
.about-text{left:287px;top:690px;width:186px;font-size:8.5px;line-height:14.2px;color:#888;text-align:justify}

/* blog */
.post{left:508px;width:196px;border-top:1px solid var(--line);padding-top:6px}
.post h3{font-size:9.5px;font-weight:700;color:var(--ink);display:flex;justify-content:space-between}
.post h3 em{font-weight:400;color:var(--blue);font-size:8.5px}
.post p{font-style:italic;font-size:7.5px;line-height:10px;color:#999;margin-top:4px}
.post .more{text-align:right;font-style:italic;font-weight:700;font-size:7.5px;color:var(--blue);margin-top:2px}

.totop{left:738px;top:847px;width:22px;height:23px;background:var(--ink);color:#fff;text-align:center;line-height:22px;font-size:11px}

/* footer */
.footer{left:0;top:870px;width:790px;height:293px;background:var(--footer)}
.fcol{top:890px;color:#ddd}
.fcol h4{font-family:"Francois One",Arial,sans-serif;font-weight:400;font-size:12.5px;color:var(--white);letter-spacing:.5px;margin-top:10px}
.links{list-style:none;margin-top:14px}
.links li{display:flex;align-items:center;gap:7px;font-style:italic;font-size:8px;color:#ddd;height:20px;margin-bottom:11px}
.ring{width:20px;height:20px;border:1.5px solid var(--blue);border-radius:50%;display:flex;align-items:center;justify-content:center}
.loc-text{font-size:8.5px;line-height:12px;margin-top:12px;width:130px}
.contact{display:flex;align-items:center;gap:9px;font-size:8.5px;margin-top:14px}
.contact .dot{width:20px;height:20px;background:#fff;border-radius:50%;display:flex;align-items:center;justify-content:center}
.news-text{font-style:italic;font-size:7.5px;line-height:10px;margin-top:10px;width:132px}
.input{width:131px;height:22px;background:#fff;margin-top:11px;padding-left:7px;font-style:italic;font-size:7.5px;color:#aaa;line-height:22px}
.hours{left:561px;top:897px;width:143px;height:241px;background:var(--panel)}
.hours ul{list-style:none;margin-top:40px}
.hours li{display:flex;align-items:center;height:22.5px;border-bottom:1px solid #1f5a89;font-size:7.5px;color:var(--blue);padding-left:15px}
.hours li b{font-weight:400;width:22px}
.hours li i{width:14px;border-top:1px solid var(--blue);margin-right:8px}
.copyright{left:0;top:1163px;width:790px;height:37px;background:var(--blue);color:#fff;font-size:8.5px;text-align:center;line-height:37px}
</style>
</head>
<body>

<div class="abs topbar">
  <div class="abs phone">
    <svg width="9" height="9" viewBox="0 0 10 10"><path d="M2 0.5 L4 2.8 L3 4 Q4.5 6 6 7 L7.2 6 L9.5 8 L8 9.5 Q3 9 0.5 2 Z" fill="#1b90e0"/></svg>
    1-800-555-0199
  </div>
  <div class="abs social" aria-label="Social links"><span></span><span></span><span></span></div>
</div>

<div class="abs brand">Brightleaf<br>Well</div>

<nav class="abs nav">
  <a href="#"><svg width="22" height="22" viewBox="0 0 22 22"><circle cx="11" cy="11" r="10" fill="none" stroke="#fff" stroke-width="1.3"/><rect x="10.2" y="9.5" width="1.6" height="7" fill="#fff"/><circle cx="11" cy="6.7" r="1.1" fill="#fff"/></svg>About Dr. Taver</a>
  <a href="#"><svg width="22" height="22" viewBox="0 0 22 22"><circle cx="11" cy="11" r="10" fill="none" stroke="#fff" stroke-width="1.3"/><path d="M6 10 H16 L15 15 H7 Z M8.5 10 L11 6.5 L13.5 10" fill="none" stroke="#fff" stroke-width="1.2"/></svg>Store</a>
  <a href="#"><svg width="22" height="22" viewBox="0 0 22 22"><circle cx="11" cy="11" r="10" fill="none" stroke="#fff" stroke-width="1.3"/><path d="M6 8 H16 V13 H10 L7.5 15.5 V13 H6 Z" fill="none" stroke="#fff" stroke-width="1.2"/></svg>Blog</a>
  <a href="#"><svg width="22" height="22" viewBox="0 0 22 22"><circle cx="11" cy="11" r="10" fill="none" stroke="#fff" stroke-width="1.3"/><rect x="6" y="8" width="8" height="6" fill="none" stroke="#fff" stroke-width="1.2"/><path d="M14 11 L17 8.5 V13.5 Z" fill="none" stroke="#fff" stroke-width="1.2"/></svg>Videos</a>
  <a href="#"><svg width="22" height="22" viewBox="0 0 22 22"><circle cx="11" cy="11" r="10" fill="none" stroke="#fff" stroke-width="1.3"/><path d="M7 15 L8 12 L14 6 L16 8 L10 14 Z" fill="none" stroke="#fff" stroke-width="1.2"/></svg>Appointment</a>
</nav>

<section class="abs hero" role="img" aria-label="Doctor touching a glowing hexagon display beside a supplement bottle"></section>
<div class="abs hero-text">
  <h1>The Best Anti-ageing<br>Integrative Medicine</h1>
  <p>The best all the healing worlds - modern<br>westeren medicine blended with centuries<br>old oriental wisdom</p>
</div>
<div class="abs dots"><span></span><span></span><span></span></div>

<h2 class="abs section-title" style="left:87px;top:366px">Our Products</h2>
<div class="abs arrows"><span>&#8249;</span><span>&#8250;</span></div>

<article class="abs product" style="left:87px">
  <div class="shot" role="img" aria-label="Supplement bottle"></div>
  <div class="label">Pain Control Medicine</div>
  <p>Lorem ipsum dolor sit amet, conse adipiscing elit, sed diam nonummy</p>
  <div class="shop"><span>SHOP NOW</span><i></i></div>
</article>
<article class="abs product" style="left:232px">
  <div class="shot" role="img" aria-label="Supplement bottle"></div>
  <div class="label">Pain Control Medicine</div>
  <p>Lorem ipsum dolor sit amet, conse adipiscing elit, sed diam nonummy</p>
  <div class="shop"><span>SHOP NOW</span><i></i></div>
</article>
<article class="abs product" style="left:378px">
  <div class="shot" role="img" aria-label="Supplement bottle"></div>
  <div class="label">Pain Control Medicine</div>
  <p>Lorem ipsum dolor sit amet, conse adipiscing elit, sed diam nonummy</p>
  <div class="shop"><span>SHOP NOW</span><i></i></div>
</article>

<h2 class="abs section-title" style="left:508px;top:366px">Make An Appointment</h2>
<p class="abs appt-intro">Lorem ipsum dolor sit amet, consectetuer adipiscing elit, sed diam nonummy nibh euismod tincidunt Lorem ipsum dolor sit amet</p>
<form class="abs form">
  <div class="field"><span class="ico"><svg width="11" height="11" viewBox="0 0 12 12"><circle cx="6" cy="3.5" r="2.6" fill="#fff"/><path d="M1 12 Q6 5 11 12 Z" fill="#fff"/></svg></span><span class="ph">Full Name</span></div>
  <div class="field"><span class="ico alt"><svg width="11" height="11" viewBox="0 0 10 10"><path d="M2 0.5 L4 2.8 L3 4 Q4.5 6 6 7 L7.2 6 L9.5 8 L8 9.5 Q3 9 0.5 2 Z" fill="none" stroke="#fff" stroke-width="1"/></svg></span><span class="ph">Phone Number</span></div>
  <div class="field"><span class="ico"><svg width="12" height="9" viewBox="0 0 12 9"><rect x="0.5" y="0.5" width="11" height="8" fill="none" stroke="#fff"/><path d="M0.5 0.5 L6 5 L11.5 0.5" fill="none" stroke="#fff"/></svg></span><span class="ph">Email Address</span></div>
  <div class="field"><span class="ico alt"><svg width="12" height="12" viewBox="0 0 12 12"><rect x="0.5" y="1.5" width="11" height="10" fill="none" stroke="#fff"/><rect x="0.5" y="1.5" width="11" height="2.5" fill="#fff"/><rect x="3" y="6" width="2" height="2" fill="#fff"/><rect x="7" y="6" width="2" height="2" fill="#fff"/></svg></span><span class="ph">Appointment Date</span></div>
  <div class="field msg"><span class="ico"><svg width="12" height="11" viewBox="0 0 12 11"><rect y="0" width="12" height="1.6" fill="#fff"/><rect y="3" width="12" height="1.6" fill="#fff"/><rect y="6" width="12" height="1.6" fill="#fff"/><rect y="9" width="8" height="1.6" fill="#fff"/></svg></span><span class="ph">Message</span></div>
</form>
<div class="abs btn" style="left:508px;top:603px;width:80px">SEND MESSAGE</div>

<h2 class="abs section-title" style="left:87px;top:654px">About Brightleaf Well</h2>
<div class="abs about-box"></div>
<div class="abs video">
  <div class="frame" role="img" aria-label="Video still of medicine bottles and tablets on a table"></div>
  <svg class="abs" style="left:62px;top:34px" width="46" height="46" viewBox="0 0 46 46"><circle cx="23" cy="23" r="20" fill="rgba(255,255,255,.25)" stroke="#fff" stroke-width="3"/><path d="M18 13 L33 23 L18 33 Z" fill="#fff"/></svg>
  <div class="bar"><span>&#9654;</span><span>00:00</span><i></i><span>00:00</span><span>&#9646;&#9646;&#9646;</span></div>
</div>
<p class="abs about-text">Lorem Ipsum has been the industry's standard dummy text ever since the 1500s, when an unknown printer took a galley of type and scrambled it to make a type specimen book.Lorem Ipsum has been the industry's standard dummy text ever since the 1500sNulla facilisiNam elit mi</p>
<div class="abs btn" style="left:287px;top:800px;width:64px">READ MORE</div>

<h2 class="abs section-title" style="left:508px;top:654px">From The Blog</h2>
<article class="abs post" style="top:680px">
  <h3>Lorem ipsum dolor sit amet <em>20 Dec, 2014</em></h3>
  <p>Lorem ipsum dolor sit amet, consectetuer adipiscing elit, sed diam nonummy nibh euismod tincidunt</p>
  <div class="more">READMORE &#8250;</div>
</article>
<article class="abs post" style="top:740px">
  <h3>Lorem ipsum dolor sit amet <em>20 Dec, 2014</em></h3>
  <p>Lorem ipsum dolor sit amet, consectetuer adipiscing elit, sed diam nonummy nibh euismod tincidunt</p>
  <div class="more">READMORE &#8250;</div>
</article>
<div class="abs btn" style="left:508px;top:800px;width:82px">READ ALL POSTS</div>
<div class="abs" style="left:590px;top:812px;width:114px;border-top:1px solid var(--line)"></div>

<div class="abs totop">&#8963;</div>

<footer class="abs footer"></footer>

<div class="abs fcol" style="left:89px">
  <svg width="52" height="52" viewBox="0 0 52 52"><circle cx="26" cy="26" r="25" fill="#1b90e0"/><path d="M17 15 L37 26 L28 28 L33 37 L29 39 L24 30 L18 36 Z" fill="#252525"/></svg>
  <h4>QUICK LINKS</h4>
  <ul class="links">
    <li><span class="ring"><svg width="6" height="8" viewBox="0 0 6 8"><path d="M1 1 L5 4 L1 7" fill="none" stroke="#ddd"/></svg></span>ABOUT TAVER CLINIC</li>
    <li><span class="ring"><svg width="6" height="8" viewBox="0 0 6 8"><path d="M1 1 L5 4 L1 7" fill="none" stroke="#ddd"/></svg></span>CHECK OUR STORE</li>
    <li><span class="ring"><svg width="6" height="8" viewBox="0 0 6 8"><path d="M1 1 L5 4 L1 7" fill="none" stroke="#ddd"/></svg></span>BLOG POSTS</li>
    <li><span class="ring"><svg width="6" height="8" viewBox="0 0 6 8"><path d="M1 1 L5 4 L1 7" fill="none" stroke="#ddd"/></svg></span>WATCH OUT VIDEOS</li>
    <li><span class="ring"><svg width="6" height="8" viewBox="0 0 6 8"><path d="M1 1 L5 4 L1 7" fill="none" stroke="#ddd"/></svg></span>MAKE AN APPOINTMENT</li>
  </ul>
</div>

<div class="abs fcol" style="left:236px">
  <svg width="52" height="52" viewBox="0 0 52 52"><circle cx="26" cy="26" r="25" fill="#1b90e0"/><path d="M26 40 Q16 28 16 22 A10 10 0 0 1 36 22 Q36 28 26 40 Z" fill="#252525"/><circle cx="26" cy="22" r="4" fill="#1b90e0"/></svg>
  <h4>LOCATION</h4>
  <p class="loc-text">Address will appear here, some details. City name. Country.</p>
  <div class="contact"><span class="dot"><svg width="9" height="9" viewBox="0 0 10 10"><path d="M2 0.5 L4 2.8 L3 4 Q4.5 6 6 7 L7.2 6 L9.5 8 L8 9.5 Q3 9 0.5 2 Z" fill="#252525"/></svg></span>1-800-555-0199</div>
  <div class="contact" style="margin-top:16px"><span class="dot"><svg width="10" height="8" viewBox="0 0 12 9"><rect x="0.5" y="0.5" width="11" height="8" fill="#252525"/><path d="M0.5 0.5 L6 5 L11.5 0.5" fill="none" stroke="#fff"/></svg></span>care@brightleafwell.com</div>
  <div class="contact" style="margin-top:16px"><span class="dot"><svg width="10" height="9" viewBox="0 0 12 11"><path d="M1 1 H11 V7 H5 L2.5 9.5 V7 H1 Z" fill="#252525"/></svg></span>Medical Chat Name</div>
</div>

<div class="abs fcol" style="left:397px">
  <svg width="52" height="52" viewBox="0 0 52 52"><circle cx="26" cy="26" r="25" fill="#1b90e0"/><path d="M15 38 L17 31 L32 16 L37 21 L22 36 Z" fill="#252525"/></svg>
  <h4>NEWSLETTER SIGN UP</h4>
  <p class="news-text">Lorem ipsum dolor sit amet, consectetuer adipiscing elit, sed diam nonummy nibh euismod tincidunt</p>
  <div class="input">Name</div>
  <div class="input">Email Address</div>
  <div class="btn" style="width:131px;margin-top:11px;height:22px;line-height:22px">SIGN UP FOR NEWSLETTER</div>
</div>

<div class="abs hours">
  <svg class="abs" style="left:49px;top:-14px" width="46" height="46" viewBox="0 0 46 46"><circle cx="23" cy="23" r="22" fill="#1b90e0"/><circle cx="23" cy="23" r="13" fill="none" stroke="#252525" stroke-width="4"/><path d="M23 15 V24 H30" fill="none" stroke="#252525" stroke-width="3"/></svg>
  <ul>
    <li><b>Mon</b><i></i>08:00 am - 12:00 pm</li>
    <li><b>Tue</b><i></i>01:00 am - 05:00 pm</li>
    <li><b>Wed</b><i></i>Free day</li>
    <li><b>Thu</b><i></i>08:00 am - 12:00 pm</li>
    <li><b>Fri</b><i></i>08:00 am - 12:00 pm</li>
    <li><b>Sat</b><i></i>08:00 am - 12:00 pm</li>
    <li style="border-bottom:0"><b>Sun</b><i></i>Free day</li>
  </ul>
  <div class="btn abs" style="left:15px;top:199px;width:111px;height:26px;line-height:26px">MAKE AN APPOINTMENT</div>
</div>

<div class="abs copyright">Copyright © 2015 BrightleafWell. All Rights Reserved.</div>

</body>
</html>
```